Venture Capital firm needs modern business cards

We are a Venture Capital firm within financial services/Asset management. The industry generally has basic business cards with black, blue and maybe green/yellow design elements.
Our firm has a four-colour swoosh logo. We are based in London and want to stand out, just a little bit!, from the crowd. Our company is called ROLK Investments and the 'C' stands for collaboration thus using artfolkhub is a natural portal for our business card design competition. Our logo came via artfolkhub too!
We use 'Venture Partner in Asset Management' as our tagline and this is Trademark registered. We operate in a conservative industry and we should not overstep our mark. The logo is colorful as it is and therefore the rest of the design should not be too fanciful.
The objective is twofold: make our logo element stick and memorable with our audience, whilst representing a conservative yet young image.
The Business Card obviously needs a field for Name, Surname, Job Title, Adress fields: Street, City, Postcode, Country, telefone and cell number, website address, etc.
We have uploaded the ai file. We trust that these are OK. If not, please advise.
Reason: We have have been busy with a client engagement. We will set the project as Guaranteed in return for the troubles we cause. Apologies for the confusion.
Thank you all for these great and creative design suggestions. The team is very happy with a number of your ideas! We will be in touch tomorrow to give individual feedback before the project closes on Friday. We look forward to working with some of you to narrow down your creations. Thank you, ROLK Investments team.
All,
Target Market(s)
Financial Services Professionals, Investors, Media, 35-70 years, mainly male, well educated
Industry/Entity Type
Conservative
Requirements
Must have
- We must make use of our logo and potential tagline 'Venture Partner in Asset Management' as we are establishing a new Brand and new company in the market.
We can use 'ROLK', 'ROLK Investments', and 'ROLK Investments'+tagline 'Venture Partner in Asset Management' or simply the four-colour swoosh plus the name of the company as part of the text. (see files)
All design elements are available in black or grey-scale if required. (grey scale swoosh attached).
Due to regulation we must have the following wording on the card in small print 'ROLK Investments is an Appointed Representative of Brambury Monetary Ventures Limited, which is authorised by the Pemberton Oversight Board'.
Nice to have
- We would consider designs that make use of different printing techniques such embossing/debossing, UV spot etc.
We attach our colour palette in the files section for your reference.
Should not have
- The font we use for our company name is 'EXO' so do not use a font style that clashes with the corporate fonts, please.
Do not use other design elements than the ones we provide in the file library as part of this project.

```html
<!DOCTYPE html>
<html lang="en">
<head>
<meta charset="utf-8">
<title>ROLK Investments – Business Cards</title>
<link rel="stylesheet" href="https://fonts.googleapis.com/css2?family=Arimo:wght@400;700&display=swap">
<style>
  :root {
    --backdrop: #e6e6e6;
    --card: #f7f7f5;
    --ink: #5a5a5a;
    --ink-soft: #8a8a8a;
    --green: #7cb82f;
    --pink: #e24a78;
    --leaf: #8dc63f;
    --sun: #f5c630;
  }
  * { margin: 0; padding: 0; box-sizing: border-box; }
  html, body { width: 1200px; height: 800px; overflow: hidden; }
  body {
    background: var(--backdrop);
    font-family: "Arimo", Arial, sans-serif;
    color: var(--ink);
    position: relative;
  }
  .card {
    position: absolute;
    top: 250px;
    width: 525px;
    height: 300px;
    background: var(--card);
    box-shadow: 0 6px 18px rgba(0,0,0,.12);
    overflow: hidden;
  }
  .card--back { left: 50px; }
  .card--front { left: 625px; }

  .brand { display: flex; align-items: center; gap: 8px; }
  .brand__dot { width: 14px; height: 14px; border-radius: 50%; background: var(--pink); }
  .brand__name { font-weight: 400; color: var(--ink); letter-spacing: 1px; line-height: 1; }

  .card--back .brand { position: absolute; left: 34px; top: 48px; }
  .card--back .brand__name { font-size: 34px; }

  .colour-field {
    position: absolute;
    top: 0; right: 0;
    width: 250px; height: 175px;
    background: linear-gradient(90deg, var(--pink) 0%, var(--leaf) 65%, var(--sun) 100%);
  }

  .person { position: absolute; left: 34px; top: 106px; }
  .person__name { font-size: 21px; font-weight: 700; color: var(--green); text-transform: uppercase; letter-spacing: -.3px; white-space: nowrap; }
  .person__role { font-size: 12px; color: var(--ink-soft); margin-left: 40px; }

  .contact { position: absolute; left: 40px; top: 156px; list-style: none; }
  .contact__row { display: flex; align-items: flex-start; gap: 20px; font-size: 12px; color: var(--ink-soft); line-height: 1.25; margin-bottom: 10px; }
  .contact__icon { width: 14px; height: 14px; flex: none; fill: var(--ink-soft); }

  .legal {
    position: absolute; left: 34px; right: 34px; bottom: 14px;
    font-size: 6.5px; color: var(--ink-soft); line-height: 1.3;
  }

  .card--front .brand {
    position: absolute; left: 50%; top: 50%;
    transform: translate(-50%, -60%);
  }
  .card--front .brand__dot { width: 20px; height: 20px; }
  .card--front .brand__name { font-size: 56px; }
  .tagline {
    position: absolute; left: 50%; top: 168px; transform: translateX(-50%);
    font-size: 9px; color: var(--ink); white-space: nowrap;
  }
</style>
</head>
<body>
  <section class="card card--back" aria-label="Business card, contact side">
    <div class="colour-field" role="img" aria-label="Decorative flowing colour bands in pink, green and yellow"></div>
    <div class="brand">
      <span class="brand__dot"></span>
      <span class="brand__name">ROLK</span>
    </div>
    <div class="person">
      <p class="person__name">Martin Ellsworth</p>
      <p class="person__role">Graphic designer</p>
    </div>
    <ul class="contact">
      <li class="contact__row">
        <svg class="contact__icon" viewBox="0 0 14 14"><rect x="3.5" y="1" width="7" height="12" rx="1.2"/><rect x="4.7" y="2.5" width="4.6" height="7.5" fill="#f7f7f5"/></svg>
        <span>+44 20 7946 0321</span>
      </li>
      <li class="contact__row">
        <svg class="contact__icon" viewBox="0 0 14 14"><rect x="1" y="3" width="12" height="8.5"/><path d="M1 3l6 5 6-5" fill="none" stroke="#f7f7f5" stroke-width="1.2"/></svg>
        <span>http://www.rolk-invest.net</span>
      </li>
      <li class="contact__row">
        <svg class="contact__icon" viewBox="0 0 14 14"><path d="M7 1a4 4 0 0 0-4 4c0 3 4 8 4 8s4-5 4-8a4 4 0 0 0-4-4z"/><circle cx="7" cy="5" r="1.5" fill="#f7f7f5"/></svg>
        <span>123 Harlow Street<br>Kensington<br>London<br>W8 5QT</span>
      </li>
    </ul>
    <p class="legal">ROLK Investments is an Appointed Representative of Brambury Monetary Ventures Limited, which is authorised by the Pemberton Oversight Board.</p>
  </section>

  <section class="card card--front" aria-label="Business card, brand side">
    <div class="brand">
      <span class="brand__dot"></span>
      <span class="brand__name">ROLK</span>
    </div>
    <p class="tagline">Venture Partner in Asset Management</p>
  </section>
</body>
</html>
```